Web Design Project for a new download application :-)

We need a website design and a logo design for a new website and desktop application.
The Website will be www.Fetchora.com
The installed application will be: Fetchora

Fetchora is a desktop application that searches and finds all kind of Media files (Movies, Games, Songs, software, etc..)
Fetchora will also manage the download process for the selected files.
Fetchora automates the whole search and download process.

User Flow:
users will initially visit the website.
user will download the application from the website
user will install the application on his computer.
user will run and use the application.

What makes our software special:
-Great search engine for searching media files.
-Very high speed downloads. maximum speeds.
-Allow used to Search by: file type, size, date, format
-Pause and resume downloads
-Get any file you want instantly.
-Unlimited Downloads.

We will need:
Logo
WebSite Design
Icons for the desktop application.

we need only PSDs - no codded pages are needed !

Design to the following screen Size & resolution: 1024 x 768

Target Market(s)

movies and music lovers.
users who download movies, games, softwares, music etc...

Industry/Entity Type

Software

Requirements
Must have
• must have download button

Files

```html
<!DOCTYPE html>
<html lang="en">
<head>
<meta charset="utf-8">
<title>Fetchora – Desktop Application</title>
<link rel="stylesheet" href="https://fonts.googleapis.com/css2?family=Arimo:wght@400;700&family=Play:wght@400;700&family=Roboto+Condensed:wght@700&display=swap">
<style>
:root{
  --page:#e8e8e8;
  --panel:#fafafa;
  --panel-edge:#cfcfcf;
  --ink:#2b2b2b;
  --text:#555;
  --muted:#777;
  --red:#b3200c;
  --red-dark:#8e1806;
  --green:#8cc21f;
  --green-dark:#6a9a10;
  --pink:#e0115f;
  --tile:#f2f2f2;
}
*{box-sizing:border-box;margin:0;padding:0}
html,body{width:940px;height:1200px;overflow:hidden}
body{background:var(--page);font-family:"Arimo",Arial,sans-serif;color:var(--text);position:relative}
.panel{position:absolute;left:11px;width:918px;background:var(--panel);border:1px solid var(--panel-edge);border-radius:5px;box-shadow:0 1px 3px rgba(0,0,0,.12)}

/* header */
.site-header{position:absolute;left:11px;top:0;width:918px;height:88px;background:linear-gradient(#fff,#f0f0f0);border:1px solid var(--panel-edge);border-top:0;border-radius:0 0 5px 5px}
.brand{position:absolute;left:16px;top:26px;display:flex;align-items:center;gap:8px;font-weight:700;font-size:28px;color:var(--ink)}
.brand-mark{width:14px;height:14px;background:var(--red);border-radius:50%}
.language{position:absolute;right:24px;top:34px;font-size:12px;color:#444;display:flex;align-items:center;gap:10px}
.flag{width:18px;height:11px;background:#1e3f8f;border:1px solid #999}

/* hero panel */
.hero-panel{top:107px;height:460px}
.main-nav{position:absolute;left:0;top:0;height:50px;display:flex;border-bottom:1px solid #ddd;width:100%;background:linear-gradient(#fff,#f1f1f1);border-radius:5px 5px 0 0}
.main-nav a{font-family:"Play",sans-serif;font-weight:700;font-size:15px;color:#555;text-decoration:none;padding:0 22px;line-height:50px;border-right:1px solid #ddd}
.main-nav a.active{background:linear-gradient(#c8331a,var(--red-dark));color:#fff;border-radius:5px 0 0 0;padding:0 26px}
.search{position:absolute;right:12px;top:13px;width:190px;height:26px;border-radius:13px;background:linear-gradient(#d8d8d8,#f4f4f4);border:1px solid #bbb}
.search svg{position:absolute;right:8px;top:4px}
.hero-title{position:absolute;left:40px;top:114px;width:370px;text-align:center;font-size:40px;line-height:48px;color:var(--ink);font-weight:400}
.hero-title strong{font-weight:700;color:#111}
.hero-lede{position:absolute;left:40px;top:236px;width:370px;text-align:center;font-size:13.5px;line-height:27px;color:#333}
.cta{position:absolute;top:319px;width:180px;height:51px;border-radius:6px;color:#fff;font-weight:700;font-size:22px;letter-spacing:-.5px;display:flex;align-items:center;padding-left:22px;box-shadow:0 2px 2px rgba(0,0,0,.25)}
.cta-download{left:39px;background:linear-gradient(#d8402a,var(--red-dark))}
.cta-download svg{position:absolute;right:10px;top:-8px}
.cta-buy{left:240px;background:linear-gradient(#b4e04c,var(--green-dark));padding-left:8px}
.cta-buy .card{display:inline-block;width:20px;height:12px;background:#eee;border-radius:2px;margin-left:6px}
.cta-note{position:absolute;top:388px;width:180px;text-align:center;font-size:12px;font-weight:700;color:#222}
.laptop{position:absolute;left:452px;top:104px;width:440px;height:286px;border-radius:12px 12px 4px 4px;background:linear-gradient(135deg,#2a2a2e,#555 50%,#c66aa6)}
.laptop-base{position:absolute;left:452px;top:390px;width:440px;height:12px;border-radius:0 0 14px 14px;background:linear-gradient(#e8e8e8,#999)}
.badge{position:absolute;left:470px;top:84px;width:68px;height:68px;border-radius:50%;background:var(--pink);color:#fff;font-weight:700;font-size:12px;line-height:15px;text-align:center;padding-top:19px;box-shadow:0 2px 3px rgba(0,0,0,.3)}

/* features panel */
.features-panel{top:584px;height:468px}
.ribbon{position:absolute;left:11px;top:35px;width:306px;height:38px;background:linear-gradient(#d23a1f,var(--red-dark));border-radius:5px 5px 0 0;color:#fff;font-family:"Roboto Condensed",sans-serif;font-size:17px;line-height:38px;padding-left:68px}
.carousel{position:absolute;left:20px;top:73px;width:880px;height:146px;background:linear-gradient(#e4e4e4,#cfcfcf);border:1px solid #bbb;border-radius:0 4px 4px 4px}
.carousel .arrow{position:absolute;top:40px}
.tile{position:absolute;top:5px;width:128px;height:124px;background:linear-gradient(#fff,var(--tile));border:1px solid #bbb;border-radius:3px}
.tile-art{position:absolute;left:24px;top:10px;width:80px;height:72px;border-radius:6px}
.tile-label{position:absolute;left:0;bottom:0;width:100%;height:32px;line-height:32px;text-align:center;font-size:13px;font-weight:700;color:var(--red-dark);border-top:1px solid #ccc;background:linear-gradient(#fafafa,#e6e6e6)}
.product-thumb{position:absolute;left:44px;top:256px;width:156px;height:141px;border:1px solid #ccc;background:#fff;padding:4px}
.product-thumb .shot{width:100%;height:100%;background:linear-gradient(#dde3ea,#bcc6cf)}
.price{position:absolute;left:-12px;top:-2px;height:28px;line-height:28px;background:var(--red);color:#fff;font-weight:700;font-size:15px;padding:0 8px}
.price-tab{position:absolute;left:56px;top:0;height:26px;line-height:26px;background:#bbb;color:#333;font-size:13px;padding:0 14px 0 24px;clip-path:polygon(14px 0,100% 0,100% 100%,14px 100%,0 50%)}
.product-title{position:absolute;left:216px;top:258px;font-family:"Play",sans-serif;font-size:21px;color:var(--red)}
.product-copy{position:absolute;left:216px;top:290px;width:670px;font-size:13.5px;line-height:25.5px;color:#666}
.product-copy a{color:var(--red);text-decoration:none}

/* footer */
.site-footer{top:1081px;height:84px}
.share{position:absolute;left:20px;top:18px;font-size:12px;font-weight:700;color:#222}
.share-icons{display:flex;gap:6px;margin-top:10px}
.share-icons span{width:16px;height:16px;border-radius:2px}
.footer-nav{position:absolute;left:0;width:100%;top:36px;text-align:center;font-size:11.5px;color:#444}
.footer-nav a{color:#444;text-decoration:none}
.footer-nav a.active{color:var(--red)}
.footer-brand{position:absolute;right:20px;top:18px;text-align:right}
.footer-brand .name{font-weight:700;font-size:22px;color:#c8c8c8}
.footer-brand .copy{font-size:11px;color:#666;margin-top:6px}
</style>
</head>
<body>

<header class="site-header">
  <div class="brand"><span class="brand-mark"></span>Fetchora</div>
  <div class="language">Language <span class="flag" role="img" aria-label="English flag"></span>▾</div>
</header>

<section class="panel hero-panel">
  <nav class="main-nav">
    <a href="#" class="active">Home</a><a href="#">Download</a><a href="#">Support</a><a href="#">Affiliates</a>
  </nav>
  <div class="search"><svg width="18" height="18" viewBox="0 0 18 18"><circle cx="7" cy="7" r="5" fill="none" stroke="#333" stroke-width="2"/><line x1="11" y1="11" x2="16" y2="16" stroke="#333" stroke-width="3" stroke-linecap="round"/></svg></div>

  <h1 class="hero-title">Fetchora Desktop<br><strong>Application</strong></h1>
  <p class="hero-lede">Lorem Ipsum is simply dummy text of the printing and typesetting industry. Lorem Ipsum has been the industry's</p>

  <a class="cta cta-download">Download
    <svg width="40" height="58" viewBox="0 0 40 58"><path d="M12 0h16v32h10L20 56 2 32h10z" fill="#f0c419" stroke="#b88a0a" stroke-width="1.5"/></svg>
  </a>
  <a class="cta cta-buy">Buy Now $29<span class="card"></span></a>
  <div class="cta-note" style="left:39px">30 Day Demo</div>
  <div class="cta-note" style="left:240px">Introductory Price</div>

  <div class="laptop" role="img" aria-label="Laptop showing the Fetchora application window"></div>
  <div class="laptop-base"></div>
  <div class="badge">Free<br>Updates</div>
</section>

<section class="panel features-panel">
  <div class="ribbon">LATEST FEATURES</div>
  <div class="carousel">
    <svg class="arrow" style="left:18px" width="22" height="44" viewBox="0 0 22 44"><path d="M18 2 4 22l14 20" fill="none" stroke="#aaa" stroke-width="4"/></svg>
    <div class="tile" style="left:112px"><div class="tile-art" role="img" aria-label="Games icon" style="background:linear-gradient(#8a5a2a,#c8a060)"></div><div class="tile-label">Games</div></div>
    <div class="tile" style="left:288px"><div class="tile-art" role="img" aria-label="Music headphones icon" style="background:linear-gradient(#555,#bbb)"></div><div class="tile-label">Music</div></div>
    <div class="tile" style="left:462px"><div class="tile-art" role="img" aria-label="Software box icon" style="background:linear-gradient(#6a7fb0,#c9ceda)"></div><div class="tile-label">Software</div></div>
    <div class="tile" style="left:635px"><div class="tile-art" role="img" aria-label="Movies folder icon" style="background:linear-gradient(#f26a80,#c8102e)"></div><div class="tile-label">Movies</div></div>
    <svg class="arrow" style="right:18px" width="22" height="44" viewBox="0 0 22 44"><path d="M4 2l14 20L4 42" fill="none" stroke="#aaa" stroke-width="4"/></svg>
  </div>

  <div class="product-thumb">
    <div class="shot" role="img" aria-label="Screenshot of the Fetchora application"></div>
    <span class="price">$19.00</span><span class="price-tab">Download</span>
  </div>
  <h2 class="product-title">Fetchora Desktop Application</h2>
  <p class="product-copy">Lorem Ipsum is simply dummy text of the printing and typesetting industry. Lorem Ipsum has been the industry's standard dummy text ever since the 1500s, when an unknown printer took a galley of type and scrambled. Lorem Ipsum is simply dummy text of the printing and typesetting industry. Lorem Ipsum has been the industry's standard dummy text ever since the 1500s, when an unknown printer took a galley of type and scrambled &nbsp;<a href="#">More Info...</a></p>
</section>

<footer class="panel site-footer">
  <div class="share">Share This Page
    <div class="share-icons"><span style="background:#1d6fa5"></span><span style="background:#3b5998"></span><span style="background:#2a9ad6"></span><span style="background:#e8902a"></span></div>
  </div>
  <nav class="footer-nav"><a href="#" class="active">Home</a> &nbsp;•&nbsp; <a href="#">Download</a> &nbsp;•&nbsp; <a href="#">Support</a> &nbsp;•&nbsp; <a href="#">Affiliates</a> &nbsp;•&nbsp; <a href="#">About</a> &nbsp;•&nbsp; <a href="#">Contact</a></nav>
  <div class="footer-brand"><div class="name">Fetchora</div><div class="copy">Copyright ©2011 Fetchora.com</div></div>
</footer>

</body>
</html>
```